Broschüre für Baumanagement
Zielgruppe
Baumanagement
Wir liefern von der Planung, über die notwendigen Handwerksfirmen langjährige Partner, Bauleitung alle notwenidgen Partner
Wir betreuen seit jahren Kunden aus dem Immobilienwesen, Handel usw.
Ein Ansprechpartner vond er Planung bis zur Übergabe
Aufgabenstellung
DIN A4, 2 Seiten, Modern, Fakten, Gerne nur in schwarz und weiss halten

```html
<!DOCTYPE html>
<html lang="de">
<head>
<meta charset="utf-8">
<title>STRUKTA GROUP – Broschüre Baumanagement</title>
<link href="https://fonts.googleapis.com/css2?family=Archivo+Black&family=Open+Sans:wght@400;700&display=swap" rel="stylesheet">
<style>
  :root {
    --ink: #1b1b1b;
    --paper: #f7f7f4;
    --accent: #f2e600;
    --backdrop: #a3a3a3;
    --photo-dark: #2e2e2e;
    --photo-light: #8a8a8a;
    --muted: #d8d8d8;
  }
  * { box-sizing: border-box; margin: 0; padding: 0; }
  html, body { width: 1200px; height: 900px; overflow: hidden; }
  body {
    background: var(--backdrop);
    font-family: "Open Sans", sans-serif;
    position: relative;
  }
  .page {
    position: absolute;
    top: 70px;
    width: 537px;
    height: 760px;
    background: var(--paper);
    overflow: hidden;
    box-shadow: 0 6px 18px rgba(0,0,0,.25);
  }
  .page--front { left: 43px; }
  .page--back { left: 620px; }
  .page svg.shapes { position: absolute; inset: 0; }
  .heading {
    font-family: "Archivo Black", sans-serif;
    text-transform: uppercase;
    line-height: 1.02;
  }
  .abs { position: absolute; }

  /* Front page */
  .accent-bar { left: 28px; top: 0; width: 6px; height: 150px; background: var(--accent); }
  .headline {
    left: 50px; top: 78px;
    font-family: "Archivo Black", sans-serif;
    font-size: 31px; line-height: 1.08; color: var(--ink);
  }
  .subline {
    left: 50px; top: 160px; width: 390px;
    font-weight: 700; font-size: 13px; line-height: 1.35; color: var(--ink);
  }
  .brand {
    display: flex; align-items: center; gap: 8px;
    font-family: "Open Sans", sans-serif; font-weight: 700;
    font-size: 17px; letter-spacing: .08em; color: var(--ink);
  }
  .brand__mark { width: 16px; height: 16px; background: var(--ink); }
  .brand--front { left: 300px; top: 250px; }
  .brand--back { right: 40px; bottom: 40px; }

  .story { left: 26px; top: 450px; width: 160px; color: var(--paper); }
  .story h2 { font-size: 27px; margin-bottom: 16px; }
  .story p { font-size: 10.5px; line-height: 1.5; }

  .services { left: 318px; top: 395px; width: 200px; color: var(--paper); }
  .services h2 { font-size: 27px; margin-bottom: 18px; }
  .service { margin-bottom: 20px; }
  .service__head { display: flex; align-items: center; gap: 10px; margin-bottom: 6px; }
  .service__num {
    width: 27px; height: 27px; background: var(--accent); color: var(--ink);
    font-family: "Archivo Black", sans-serif; font-size: 16px;
    display: flex; align-items: center; justify-content: center;
  }
  .service__title { font-family: "Archivo Black", sans-serif; font-size: 13px; line-height: 1.1; }
  .service p { font-size: 10.5px; line-height: 1.4; color: var(--muted); }

  /* Back page */
  .process-title { left: 40px; top: 40px; font-size: 30px; color: var(--paper); }
  .step-label {
    font-family: "Archivo Black", sans-serif; font-size: 12.5px; line-height: 1.15;
    color: var(--paper); border-bottom: 1px solid var(--paper); padding-bottom: 4px; width: 110px;
  }
  .step-text { font-size: 10px; line-height: 1.4; color: var(--muted); width: 130px; }
  .contact { left: 205px; top: 500px; color: var(--ink); }
  .contact h2 { font-size: 26px; margin-bottom: 8px; }
  .contact p { font-size: 11px; line-height: 1.45; }
</style>
</head>
<body>

<article class="page page--front">
  <svg class="shapes" width="537" height="760" viewBox="0 0 537 760">
    <defs>
      <linearGradient id="siteGrad" x1="0" y1="0" x2="0" y2="1">
        <stop offset="0" stop-color="var(--photo-light)"/>
        <stop offset="1" stop-color="var(--photo-dark)"/>
      </linearGradient>
    </defs>
    <polygon points="150,360 300,330 300,760 150,760" fill="url(#siteGrad)" role="img" aria-label="Foto: Bauleiter auf einer Baustelle"/>
    <polygon class="story-panel" points="0,360 205,420 205,760 0,760" fill="var(--ink)"/>
    <polygon class="services-panel" points="300,400 410,290 537,450 537,760 300,760" fill="var(--ink)"/>
    <rect x="296" y="395" width="5" height="365" fill="var(--accent)"/>
  </svg>

  <div class="abs accent-bar"></div>
  <h1 class="abs headline">STRUKTA -<br>Alles aus einer Hand</h1>
  <p class="abs subline">Von der Planung bis zur Übergabe – Ihr verlässlicher Partner für erfolgreiche Bauprojekte.</p>
  <div class="abs brand brand--front"><span>STRUKTA</span><span class="brand__mark"></span><span>GROUP</span></div>

  <section class="abs story">
    <h2 class="heading">Unsere<br>Story</h2>
    <p>Seit Jahren begleiten wir unsere Kunden aus der Immobilienbranche, dem Handel und weiteren Bereichen durch alle Phasen eines Bauprojekts. Mit einem starken Netzwerk aus erfahrenen Partnern und umfassender Expertise im Baumanagement sorgen wir dafür, dass jedes Projekt termingerecht, effizient und hochwertig realisiert wird.</p>
  </section>

  <section class="abs services">
    <h2 class="heading">Leist-<br>ungen</h2>
    <div class="service">
      <div class="service__head"><span class="service__num">1</span><span class="service__title">Planung</span></div>
      <p>Entwicklung individueller Baukonzepte und Abstimmung mit Architekten und Fachplanern.</p>
    </div>
    <div class="service">
      <div class="service__head"><span class="service__num">2</span><span class="service__title">Partner-<br>netzwerk</span></div>
      <p>Langjährige Zusammenarbeit mit zuverlässigen Handwerksfirmen und Komplettlösung durch erfahrene Spezialisten.</p>
    </div>
    <div class="service">
      <div class="service__head"><span class="service__num">3</span><span class="service__title">Bauleitung</span></div>
      <p>Koordination aller Gewerke und Überwachung von Zeit- und Kostenplänen.</p>
    </div>
    <div class="service">
      <div class="service__head"><span class="service__num">4</span><span class="service__title">Übergabe</span></div>
      <p>Qualitätssicherung bis zur schlüsselfertigen Übergabe.</p>
    </div>
  </section>
</article>

<article class="page page--back">
  <svg class="shapes" width="537" height="760" viewBox="0 0 537 760">
    <defs>
      <linearGradient id="portraitGrad" x1="0" y1="0" x2="1" y2="1">
        <stop offset="0" stop-color="var(--photo-light)"/>
        <stop offset="1" stop-color="var(--photo-dark)"/>
      </linearGradient>
    </defs>
    <polygon class="process-panel" points="0,0 537,0 537,150 370,150 370,330 230,470 0,470" fill="var(--ink)"/>
    <polygon points="370,150 515,150 515,485 450,485 370,400" fill="url(#portraitGrad)" role="img" aria-label="Foto: Bauleiter mit Schutzhelm beim Telefonieren"/>
    <rect x="515" y="150" width="5" height="345" fill="var(--accent)"/>
    <g class="process-path" stroke="var(--accent)" stroke-width="2" fill="none">
      <polyline points="262,148 196,218 252,296 168,362"/>
    </g>
    <g fill="var(--accent)">
      <rect x="248" y="134" width="28" height="28"/>
      <rect x="182" y="204" width="28" height="28"/>
      <rect x="238" y="282" width="28" height="28"/>
      <rect x="154" y="348" width="28" height="28"/>
    </g>
  </svg>

  <h2 class="abs heading process-title">Prozess</h2>

  <p class="abs step-text" style="left:100px; top:100px;">Wir analysieren Ihre Anforderungen und erstellen ein passgenaues Konzept.</p>
  <div class="abs step-label" style="left:290px; top:132px;">Beratung<br>&amp; Planung</div>

  <div class="abs step-label" style="left:60px; top:200px;">Auswahl<br>der Partner</div>
  <p class="abs step-text" style="left:222px; top:206px;">Wir wählen die passenden Fachleute aus unserem Netzwerk.</p>

  <p class="abs step-text" style="left:95px; top:276px;">Wir steuern und koordinieren den gesamten Bauprozess.</p>
  <div class="abs step-label" style="left:280px; top:280px;">Realisie-<br>rung</div>

  <p class="abs step-text" style="left:195px; top:352px;">Termintreu, transparent, zuverlässig.</p>

  <section class="abs contact">
    <h2 class="heading">Kontakt</h2>
    <p>Beispielweg 7, Nordstadt<br>kontakt@strukta-bau.de<br>www.strukta-bau.de<br>0987 654321</p>
  </section>

  <div class="abs brand brand--back"><span>STRUKTA</span><span class="brand__mark"></span><span>GROUP</span></div>
</article>

</body>
</html>
```